Customer Upgrade from Free to Paid Investment Management

Our intent is to have customers that use our free online service consider converting into our paid investment management service.

In current vernacular, we have a Freemium business proposition - but we are just at the early stages of building out our upgrade capabilities.

The design request is detailed in the attached file, but essentially, I'm looking to add another banner to our library. Let me see what you can do!

Target Market(s)

40s-50s, can have any balance in their 401k, at first thought they could manage their 401k themselves, but may be interested in having us manage.

Industry/Entity Type

Investment

Requirements
Must have
• Keep it very simple.
Banner specs are attached in the file
Should not have
• No animation
No "hard sell"

```html
<!DOCTYPE html>
<html lang="en">
<head>
<meta charset="UTF-8">
<title>Professional Management Banner</title>
<link href="https://fonts.googleapis.com/css2?family=Arimo:wght@400;700&display=swap" rel="stylesheet">
<style>
  :root {
    --page-bg: #ffffff;
    --panel-top: #f4fbfe;
    --panel-bottom: #d3ecf8;
    --panel-edge: #b9dcee;
    --navy: #0e3f7f;
    --bar-dark: #2b2b2b;
    --bar-light: #5a5a5a;
    --bar-text: #ffffff;
    --green-top: #76c043;
    --green-bottom: #3f8f1f;
    --green-edge: #2f7616;
    --frame: #ffffff;
    --frame-edge: #c9c9c9;
    --photo-a: #b7b0ac;
    --photo-b: #5b4438;
  }
  * { box-sizing: border-box; margin: 0; padding: 0; }
  html, body {
    width: 1200px;
    height: 174px;
    overflow: hidden;
    background: var(--page-bg);
    font-family: "Arimo", Arial, sans-serif;
  }
  .banner {
    position: relative;
    width: 1200px;
    height: 174px;
  }
  .banner__panel {
    position: absolute;
    left: 200px;
    top: 20px;
    width: 996px;
    height: 150px;
    background: linear-gradient(180deg, var(--panel-top) 0%, var(--panel-bottom) 100%);
    border: 2px solid var(--panel-edge);
    border-left: none;
    border-radius: 0 22px 0 0;
  }
  .banner__portrait {
    position: absolute;
    left: 10px;
    top: 4px;
    width: 228px;
    height: 166px;
    background: var(--frame);
    border: 2px solid var(--frame-edge);
    padding: 8px;
    box-shadow: 0 2px 4px rgba(0,0,0,0.15);
  }
  .banner__portrait-fill {
    width: 100%;
    height: 100%;
    background: linear-gradient(180deg, var(--photo-a) 0%, var(--photo-b) 100%);
  }
  .banner__headline {
    position: absolute;
    left: 275px;
    top: 66px;
    font-size: 40px;
    font-weight: 700;
    color: var(--navy);
    letter-spacing: 0.2px;
    line-height: 1;
  }
  .banner__subbar {
    position: absolute;
    left: 252px;
    top: 124px;
    width: 790px;
    height: 44px;
    background: linear-gradient(180deg, var(--bar-light) 0%, var(--bar-dark) 55%);
    border-radius: 22px 0 0 22px;
    display: flex;
    align-items: center;
    padding-left: 30px;
  }
  .banner__subtext {
    color: var(--bar-text);
    font-size: 21px;
    font-weight: 700;
  }
  .banner__cta {
    position: absolute;
    left: 1050px;
    top: 60px;
    width: 134px;
    height: 110px;
    background: linear-gradient(180deg, var(--green-top) 0%, var(--green-bottom) 100%);
    border: 2px solid var(--green-edge);
    border-radius: 10px;
    display: flex;
    align-items: center;
    justify-content: center;
    text-align: center;
    color: #ffffff;
    font-size: 29px;
    font-weight: 700;
    line-height: 1.05;
    text-decoration: none;
    text-shadow: 0 1px 2px rgba(0,0,0,0.3);
  }
</style>
</head>
<body>
  <div class="banner">
    <div class="banner__panel"></div>
    <div class="banner__portrait">
      <div class="banner__portrait-fill" role="img" aria-label="Portrait photo of a smiling investment advisor"></div>
    </div>
    <h1 class="banner__headline">Want us to manage this for you?</h1>
    <div class="banner__subbar">
      <p class="banner__subtext">Enroll in Professional Management and we will do the work</p>
    </div>
    <a class="banner__cta" href="#">Learn<br>more</a>
  </div>
</body>
</html>
```